German Webagency needs fresh modern Design

Our website is 4 years old. We need an fresh modern website. All pics we used before are from customers or handmade by us. the new website should be clear with nice handling. please dont copy something from template websites. it would be great if you can surprise us with something great. its our first project here. don´t worry if i make a mistake in responding or briefing. after 20 years you can´t see the works of your own "designer" so we hope for help :-)
our existing site: www.korvanetz.de
Target Market(s)
small and middle sized companys in germany
Number of Pages Required
4 page
Font styles to use
Colors
Designer to choose colors to be used in the design.
Requirements
Must have
- Responsive (sure we code it)
- Modern and big Font ..Headlines and Slider
- innovative..if you know something new..feel free to show
Nice to have
- the site with our works/refences should look great and later easy to handle when we code it or use wp.
- we like black and grey but if you have better ideas also feel free
Should not have
- a cup of coffe..laptop.. a pencil a handwritten font
- dont copy and modify templates from know websites..bad style

```html
<!DOCTYPE html>
<html lang="de">
<head>
<meta charset="utf-8">
<title>Korvanetz – Webdesign &amp; Grafikdesign</title>
<link rel="stylesheet" href="https://fonts.googleapis.com/css2?family=Lato:wght@400;700;900&family=Open+Sans:ital,wght@0,400;0,600;1,400&display=swap">
<style>
:root{
  --blue:#1f5bb5;
  --blue-dark:#0d3a8c;
  --blue-light:#e4effc;
  --steel:#5f7fa6;
  --ink:#111111;
  --text:#555a60;
  --grey-bg:#ececec;
  --footer:#141414;
  --white:#ffffff;
}
*{margin:0;padding:0;box-sizing:border-box}
html,body{width:1200px;height:2786px;overflow:hidden}
body{position:relative;background:var(--white);font-family:"Open Sans",Arial,sans-serif;color:var(--text)}
.abs{position:absolute}

/* header */
.logo{left:134px;top:30px;font-family:"Lato",Arial,sans-serif;font-weight:900;font-size:38px;color:var(--blue-dark);letter-spacing:-0.5px;display:flex;align-items:center;gap:10px}
.logo-dot{width:14px;height:14px;border-radius:50%;background:var(--blue)}
.nav{left:460px;top:32px;display:flex;font-family:"Lato",Arial,sans-serif;font-size:16px}
.nav a{color:#6a6a6a;text-decoration:none;height:40px;line-height:40px;padding:0 12px}
.nav a.active{background:var(--blue);color:var(--white);padding:0 21px;margin-right:8px}

/* hero */
.hero-title{left:132px;top:200px;font-family:"Lato",Arial,sans-serif;font-weight:900;font-size:41px;line-height:46px;color:var(--ink)}
.hero-title span{color:var(--blue)}
.hero-sub{left:136px;top:306px;width:340px;font-family:"Lato",Arial,sans-serif;font-weight:700;font-size:15px;line-height:20px;letter-spacing:0.6px;color:var(--steel)}
.btn-outline{display:block;border:2px solid var(--blue-dark);color:var(--blue-dark);font-family:"Lato",Arial,sans-serif;font-size:15px;font-weight:700;text-align:center;letter-spacing:0.3px;background:var(--white)}
.hero-btn{left:136px;top:390px;width:148px;height:41px;line-height:37px}
.hero-art{left:612px;top:176px;width:465px;height:372px;border-radius:6px;background:linear-gradient(135deg,#a7c4f7,#2e56b8)}
.dots{left:550px;top:572px;display:flex;gap:10px}
.dots i{width:13px;height:13px;border-radius:50%;background:var(--blue);display:block}
.dots i:first-child{background:var(--white);border:2px solid var(--blue)}

/* about */
.about-art{left:190px;top:630px;width:380px;height:440px;background:linear-gradient(180deg,#fbf3d6 0,#f6f6f6 60%,#ffffff 100%)}
.section-title{font-family:"Lato",Arial,sans-serif;font-weight:900;color:var(--ink);letter-spacing:0.5px}
.about-title{left:656px;top:716px;font-size:34px}
.about-title span{color:var(--blue-dark)}
.about-text{left:657px;top:786px;width:420px;font-size:14px;line-height:22px}
.about-text p{margin-bottom:10px}
.about-btn{left:657px;top:938px;width:147px;height:41px;line-height:37px}

/* services */
.services-title{left:0;width:1200px;top:1192px;text-align:center;font-size:31px;font-weight:700}
.card{top:1274px;width:219px;height:316px;background:var(--white);border:1px solid #d5d5d5;box-shadow:0 1px 4px rgba(0,0,0,.12);text-align:center}
.card svg{margin-top:28px}
.card h3{font-family:"Lato",Arial,sans-serif;font-weight:700;font-size:19px;line-height:22px;color:var(--blue-dark);height:48px;display:flex;align-items:center;justify-content:center;margin-top:8px}
.card .rule{width:28px;height:2px;background:#bbb;margin:6px auto 12px}
.card p{font-size:12px;line-height:18px;padding:0 22px;color:#6a6a6a;height:54px}
.card .btn-fill{display:inline-block;margin-top:16px;width:118px;height:30px;line-height:30px;border-radius:15px;background:var(--blue);color:var(--white);font-size:13px}

/* testimonials */
.testi-title{left:0;width:1200px;top:1726px;text-align:center;font-size:25px;font-weight:700;color:var(--white)}
.testi-quote{left:230px;top:1795px;width:740px;text-align:center;font-style:italic;font-size:22px;line-height:31px;color:#e8f0ff}
.testi-quote b{font-family:"Lato",Arial,sans-serif;font-style:normal;font-weight:900;font-size:44px;color:var(--white);line-height:0;vertical-align:-14px}
.avatar{left:554px;top:1900px;width:92px;height:92px;border-radius:50%;border:4px solid var(--white);background:radial-gradient(circle,#d8c0a8,#7e8da0)}
.author{left:0;width:1200px;top:2004px;text-align:center;font-family:"Lato",Arial,sans-serif;font-size:16px;color:var(--white)}

/* credentials */
.cred-title{left:0;width:1200px;top:2138px;text-align:center;font-size:29px;font-weight:700}
.shot{box-shadow:0 2px 8px rgba(0,0,0,.25)}
.view-btn{left:520px;top:2550px;width:178px;height:44px;line-height:40px;font-size:17px}

/* footer */
.footer{left:0;top:2646px;width:1200px;height:140px;background:var(--footer);border-top:8px solid var(--blue)}
.foot-nav{left:143px;top:2688px;display:flex;gap:24px;font-family:"Lato",Arial,sans-serif;font-size:16px;color:#e6e6e6}
.copyright{left:143px;top:2723px;font-size:11px;color:#bdbdbd}
.social{left:903px;top:2680px;display:flex;gap:7px}
.social i{display:block;width:36px;height:36px;border-radius:50%;border:2px solid #e6e6e6}
</style>
</head>
<body>

<!-- background shapes -->
<svg class="abs" style="left:0;top:0" width="1200" height="2786" aria-hidden="true">
  <path d="M470 600 C470 380 560 230 720 180 C800 150 780 0 860 0 L1200 0 L1200 640 Z" fill="var(--blue-light)"/>
  <path d="M0 578 L1200 610 L1200 650 L0 610 Z" fill="#dbe6f5"/>
  <path d="M0 578 L330 590 L0 612 Z" fill="var(--blue-dark)"/>
  <path d="M330 590 L0 612 L0 600 Z" fill="var(--blue)"/>
  <path d="M0 1078 L1200 1130 L1200 1640 L0 1660 Z" fill="var(--grey-bg)"/>
  <path d="M800 1140 L1200 1108 L1200 1140 Z" fill="var(--blue-dark)"/>
  <path d="M760 1142 L1200 1126 L1200 1145 Z" fill="var(--blue)"/>
  <!-- title swooshes, below the headings -->
  <path d="M630 770 C624 756 640 750 660 748" fill="none" stroke="#bbb" stroke-width="4"/>
  <path d="M486 1240 C480 1228 498 1226 540 1230" fill="none" stroke="#bbb" stroke-width="4"/>
  <path d="M476 2184 C470 2172 488 2170 530 2174" fill="none" stroke="#bbb" stroke-width="4"/>
</svg>

<!-- testimonials band -->
<div class="abs" role="img" aria-label="Team photograph behind a blue overlay" style="left:0;top:1634px;width:1200px;height:494px;background:linear-gradient(135deg,#2467c9,#1550b0 55%,#0e3f95);clip-path:polygon(0 12%,100% 0,100% 86%,0 100%)"></div>
<svg class="abs" style="left:486px;top:1752px" width="60" height="24" aria-hidden="true"><path d="M4 20 C0 10 14 8 54 10" fill="none" stroke="#9cb9e8" stroke-width="4"/></svg>

<!-- header -->
<div class="abs logo"><span class="logo-dot"></span>korvanetz.de</div>
<nav class="abs nav">
  <a class="active">HOME</a><a>ABOUT US</a><a>SERVICES</a><a>CREDENTIALS</a><a>CURRENT</a><a>CONTACT US</a>
</nav>

<!-- hero -->
<h1 class="abs hero-title">WEBDESIGN &amp;<br><span>GRAFIKDESIGN</span></h1>
<p class="abs hero-sub">WEBENTWICKLUNG • MARKETING • WEB-HOSTING • RESPONSIVE WEBDESIGN • GESCHÄFTSAUSSTATTUNG</p>
<a class="abs btn-outline hero-btn">READ MORE</a>
<div class="abs hero-art" role="img" aria-label="Illustration of two people arranging content blocks on a large browser window"></div>
<div class="abs dots"><i></i><i></i><i></i><i></i></div>

<!-- about -->
<div class="abs about-art" role="img" aria-label="Illustration of a crumpled yellow paper light bulb with a cable"></div>
<h2 class="abs section-title about-title">ABOUT <span>KORVANETZ</span></h2>
<div class="abs about-text">
  <p>Praesent elementum elit at tellus nec ultricies sit amet porttitor mattis enim In massa libero interdum nec interdum vel blandit sed nulla In ullamcorper est eget tempor</p>
  <p>Aonsectetuer mi a ultricies massa est sed nisl Class aptent taciti sociosqu ad litora torquent per</p>
</div>
<a class="abs btn-outline about-btn">READ MORE</a>

<!-- services -->
<h2 class="abs section-title services-title">OUR SERVICES</h2>

<div class="abs card" style="left:139px">
  <svg width="64" height="64" viewBox="0 0 64 64" fill="none" stroke="var(--blue-dark)" stroke-width="2"><rect x="6" y="6" width="52" height="40"/><rect x="14" y="18" width="36" height="14"/><path d="M22 46 L18 60 M42 46 L46 60 M10 12 H54"/></svg>
  <h3>Advertising<br>Measures</h3><div class="rule"></div>
  <p>Aociosqu ad litora torquent per conubia nostra per inceptos hymenaeos Proin</p>
  <a class="btn-fill">Learn More</a>
</div>
<div class="abs card" style="left:377px">
  <svg width="64" height="64" viewBox="0 0 64 64" fill="none" stroke="var(--blue-dark)" stroke-width="2"><rect x="4" y="6" width="56" height="50"/><path d="M4 14 H60"/><circle cx="32" cy="36" r="8"/><circle cx="32" cy="36" r="14" stroke-dasharray="5 4"/></svg>
  <h3>Web design &amp;<br>Web development</h3><div class="rule"></div>
  <p>Aociosqu ad litora torquent per conubia nostra per inceptos hymenaeos Proin</p>
  <a class="btn-fill">Learn More</a>
</div>
<div class="abs card" style="left:615px">
  <svg width="64" height="64" viewBox="0 0 64 64" fill="none" stroke="var(--blue-dark)" stroke-width="2"><rect x="4" y="8" width="56" height="38"/><path d="M26 46 L24 56 H40 L38 46"/><rect x="24" y="18" width="8" height="8"/><rect x="32" y="18" width="8" height="8"/><rect x="28" y="26" width="8" height="8"/></svg>
  <h3>Print Design</h3><div class="rule"></div>
  <p>Aociosqu ad litora torquent per conubia nostra per inceptos hymenaeos Proin</p>
  <a class="btn-fill">Learn More</a>
</div>
<div class="abs card" style="left:853px">
  <svg width="64" height="64" viewBox="0 0 64 64" fill="none" stroke="var(--blue-dark)" stroke-width="2"><rect x="8" y="10" width="48" height="36"/><path d="M2 50 H62 L58 56 H6 Z"/><path d="M22 24 H30 L42 16 V38 L30 30 H22 Z"/></svg>
  <h3>Direct Marketing</h3><div class="rule"></div>
  <p>Aociosqu ad litora torquent per conubia nostra per inceptos hymenaeos Proin</p>
  <a class="btn-fill">Learn More</a>
</div>

<!-- testimonials -->
<h2 class="abs section-title testi-title">TESTIMONIALS</h2>
<p class="abs testi-quote"><b>“</b> Fusce tellus Sed metus augue convallis et vehicula ut pulvinar eu ante Integer orci tellus tristique vitae consequat necVivamus porttitor purus nisi eleifend libero a tempus libero lectus feugiat felis <b>”</b></p>
<svg class="abs" style="left:514px;top:1934px" width="172" height="24" aria-hidden="true" fill="none" stroke="#cfe0ff" stroke-width="2.5"><path d="M12 2 L2 12 L12 22"/><path d="M160 2 L170 12 L160 22"/></svg>
<div class="abs avatar" role="img" aria-label="Portrait of the testimonial author"></div>
<p class="abs author">BY AUTHOR NAME</p>

<!-- credentials -->
<h2 class="abs section-title cred-title">CREDENTIALS</h2>
<div class="abs shot" role="img" aria-label="Screenshot of a transport company website with green header" style="left:78px;top:2256px;width:301px;height:223px;background:linear-gradient(180deg,#f2f5f1 0,#f2f5f1 20%,#3a8a3a 20%,#3a8a3a 26%,#eef2ee 26%,#5f8f7a 55%,#e8ece8 80%)"></div>
<div class="abs shot" role="img" aria-label="Screenshot of a housing cooperative website with green navigation" style="left:819px;top:2256px;width:295px;height:222px;background:linear-gradient(180deg,#ffffff 0,#ffffff 12%,#5aa640 12%,#5aa640 16%,#c9b49e 16%,#a89482 58%,#f4f4f4 58%)"></div>
<div class="abs shot" role="img" aria-label="Screenshot of a courier service website with a man in front of a van" style="left:379px;top:2219px;width:440px;height:288px;background:linear-gradient(135deg,#c4b05a,#8d9096 45%,#d8dade 70%,#f2cf1a);border-top:16px solid #f5d11c;border-bottom:14px solid #f5d11c"></div>
<svg class="abs" style="left:40px;top:2350px" width="1120" height="34" aria-hidden="true" fill="none" stroke="#777" stroke-width="2.5"><path d="M18 2 L4 17 L18 32"/><path d="M1102 2 L1116 17 L1102 32"/></svg>
<a class="abs btn-outline view-btn">VIEW ALL</a>

<!-- footer -->
<footer class="abs footer"></footer>
<nav class="abs foot-nav"><span>HOME</span><span>ABOUT US</span><span>SERVICES</span><span>CREDENTIALS</span><span>CURRENT</span><span>CONTACT US</span></nav>
<p class="abs copyright">© 2018 Company Name. All right reserved. Term of Use</p>
<div class="abs social" aria-label="Social links"><i></i><i></i><i></i><i></i></div>

</body>
</html>
```